SaaS Early tech startup business card design

Unique design for experience ecommerce platform company. the business cards will be used by executive members. conformance with color code is required.

```html
<!DOCTYPE html>
<html lang="en">
<head>
<meta charset="utf-8">
<title>Nuvel Business Card</title>
<link href="https://fonts.googleapis.com/css2?family=Lato:wght@400;900&family=Roboto:wght@400&display=swap" rel="stylesheet">
<style>
  :root {
    --backdrop: #222222;
    --card-white: #ffffff;
    --teal: #0f9a9c;
    --teal-bright: #06b79d;
    --teal-mid: #0ba79f;
    --teal-deep: #0a8f9a;
    --logo-blue: #137f99;
    --logo-blue-dark: #0e6a8e;
    --ink: #222222;
    --divider: #e2e2e2;
  }
  html, body {
    margin: 0;
    padding: 0;
    width: 1200px;
    height: 801px;
    overflow: hidden;
    background: var(--backdrop);
  }
  .canvas {
    position: relative;
    width: 1200px;
    height: 801px;
  }
  .card {
    position: absolute;
    top: 274px;
    width: 443px;
    height: 263px;
    overflow: hidden;
  }
  .card--front {
    left: 153px;
    background: var(--card-white);
  }
  .card--back {
    left: 625px;
  }
  .brand-name {
    position: absolute;
    margin: 0;
    font-family: "Lato", sans-serif;
    font-weight: 900;
    line-height: 1;
    letter-spacing: 1px;
  }
  .card--front .brand-name {
    left: 29px;
    top: 90px;
    font-size: 70px;
    color: var(--logo-blue);
  }
  .divider {
    position: absolute;
    left: 222px;
    top: 47px;
    width: 1px;
    height: 174px;
    background: linear-gradient(to bottom, rgba(226,226,226,0), var(--divider) 20%, var(--divider) 80%, rgba(226,226,226,0));
  }
  .details {
    position: absolute;
    left: 242px;
    top: 65px;
    font-family: "Roboto", sans-serif;
    color: var(--ink);
  }
  .person-name {
    margin: 0;
    font-family: "Lato", sans-serif;
    font-weight: 400;
    font-size: 18px;
    line-height: 22px;
    color: var(--teal);
    letter-spacing: 0.2px;
  }
  .person-title {
    margin: 0 0 8px;
    font-size: 13px;
    line-height: 16px;
  }
  .contact-list {
    list-style: none;
    margin: 0 0 8px;
    padding: 0;
  }
  .contact-list li {
    display: flex;
    align-items: center;
    gap: 4px;
    font-size: 12.5px;
    line-height: 16px;
  }
  .contact-list svg {
    width: 11px;
    height: 11px;
    flex: none;
  }
  .address {
    margin: 0;
    font-style: normal;
    font-size: 13px;
    line-height: 16px;
  }
  .back-pattern {
    position: absolute;
    inset: 0;
    background: linear-gradient(120deg, var(--teal-bright) 0%, var(--teal-mid) 45%, var(--teal-deep) 100%);
  }
  .card--back .brand-name {
    left: 128px;
    top: 96px;
    font-size: 82px;
    color: var(--logo-blue-dark);
  }
</style>
</head>
<body>
<main class="canvas">
  <section class="card card--front" aria-label="Business card front">
    <p class="brand-name">nuvel</p>
    <div class="divider"></div>
    <div class="details">
      <h1 class="person-name">DANIEL HARPER</h1>
      <p class="person-title">Managing Director</p>
      <ul class="contact-list">
        <li>
          <svg viewBox="0 0 12 12" aria-hidden="true"><path d="M2.5 1 L4.5 1 L5.2 3.4 L4 4.3 C4.6 5.7 6.3 7.4 7.7 8 L8.6 6.8 L11 7.5 L11 9.5 C11 10.3 10.3 11 9.5 11 C5 11 1 7 1 2.5 C1 1.7 1.7 1 2.5 1 Z" fill="none" stroke="#0f9a9c" stroke-width="1.2"/></svg>
          021-587 304 916
        </li>
        <li>
          <svg viewBox="0 0 12 12" aria-hidden="true"><rect x="0.5" y="2.5" width="11" height="7" fill="#0f9a9c"/><path d="M0.5 2.5 L6 7 L11.5 2.5" fill="none" stroke="#ffffff" stroke-width="0.9"/></svg>
          hello@nuvelhq.com
        </li>
        <li>
          <svg viewBox="0 0 12 12" aria-hidden="true"><g fill="none" stroke="#0f9a9c" stroke-width="1"><circle cx="6" cy="6" r="5"/><ellipse cx="6" cy="6" rx="2.2" ry="5"/><line x1="1" y1="6" x2="11" y2="6"/><line x1="2" y1="3.5" x2="10" y2="3.5"/><line x1="2" y1="8.5" x2="10" y2="8.5"/></g></svg>
          www.nuvelstudio.io
        </li>
      </ul>
      <address class="address">218, Harbor Lane, Suite 40<br>30817,Eastmoor Bay</address>
    </div>
  </section>

  <section class="card card--back" aria-label="Business card back">
    <div class="back-pattern" role="img" aria-label="Teal checkered tile pattern background"></div>
    <p class="brand-name">nuvel</p>
  </section>
</main>
</body>
</html>
```